Letterhead, business card and email signature design

I have a new company and I would like a professional letterhead, business card and email signature designed. Id like the business card to have room for a photo of the bearer. I'd also like the template to be editable so we can adapt for future members of staff etc.

```html
<!DOCTYPE html>
<html lang="en">
<head>
<meta charset="utf-8">
<title>Nimbara Networks — Stationery</title>
<link rel="stylesheet" href="https://fonts.googleapis.com/css2?family=Prompt:wght@400;500&display=swap">
<style>
  :root {
    --navy: #1b3558;
    --navy-deep: #14284a;
    --crimson: #a51e53;
    --teal: #1d4b6b;
    --paper: #ffffff;
    --card: #f5f4f5;
    --ground: #eef3f6;
    --faint: #ebecf1;
    --photo-a: #c9b5a6;
    --photo-b: #2b3646;
    --font: "Prompt", "Helvetica Neue", Arial, sans-serif;
  }
  * { box-sizing: border-box; margin: 0; padding: 0; }
  html, body { width: 899px; height: 1200px; overflow: hidden; }
  body { background: var(--ground); font-family: var(--font); position: relative; }

  .piece { position: absolute; overflow: hidden; box-shadow: 0 6px 14px rgba(20, 40, 70, .28); }
  .abs { position: absolute; }

  /* Brand lockup: plain circle + name */
  .brand { position: absolute; display: flex; align-items: center; }
  .brand-dot { border-radius: 50%; background: var(--navy); flex: none; }
  .brand-name { color: var(--navy); font-weight: 500; line-height: 1.05; letter-spacing: .02em; text-transform: uppercase; white-space: nowrap; }

  /* Letterhead */
  .letterhead { left: 30px; top: 121px; width: 480px; height: 621px; background: var(--paper); }
  .letterhead .watermark { left: 135px; top: 200px; width: 215px; height: 215px; border-radius: 50%; background: var(--faint); }
  .letterhead .band { left: 0; bottom: 0; width: 381px; height: 39px; background: var(--navy); }
  .letterhead .band-accent { right: 0; bottom: 0; width: 99px; height: 39px; background: var(--crimson); }

  /* Business cards */
  .card { width: 329px; height: 188px; background: var(--card); left: 540px; }
  .card-front { top: 121px; }
  .card-back { top: 339px; }
  .card-back .photo { left: 24px; top: 44px; width: 84px; height: 104px; border-radius: 42px 42px 8px 8px;
    background: linear-gradient(180deg, var(--photo-a) 0 55%, var(--photo-b) 55% 100%); }
  .card-back .holder { left: 140px; top: 62px; width: 175px; text-align: center; }
  .holder-name { color: var(--navy-deep); font-size: 14px; font-weight: 500; white-space: nowrap; }
  .holder-role { color: var(--crimson); font-size: 12px; margin-top: 4px; }
  .holder-phone { color: var(--crimson); font-size: 12px; font-weight: 500; margin-top: 10px;
    display: flex; justify-content: center; align-items: center; gap: 4px; }
  .card-back .band { left: 0; bottom: 0; width: 100%; height: 15px; background: var(--navy); }

  /* Envelope */
  .envelope { left: 540px; top: 557px; width: 329px; height: 185px; background: var(--card); }

  /* Email signature */
  .signature { left: 30px; top: 772px; width: 839px; height: 307px; background: var(--paper); }
  .signature .top { left: 0; top: 0; width: 100%; height: 172px; background: var(--teal); }
  .signature .photo { left: 40px; top: 32px; width: 150px; height: 205px; border-radius: 75px 75px 75px 75px / 75px 75px 90px 90px;
    background: linear-gradient(180deg, var(--photo-a) 0 52%, var(--photo-b) 52% 100%); }
  .signature .holder { left: 220px; top: 70px; width: 320px; text-align: center; }
  .signature .holder-name { color: #ffffff; font-size: 25px; }
  .signature .holder-role { font-size: 20px; margin-top: 2px; }
  .social { right: 36px; top: 74px; display: flex; gap: 16px; }
  .social span { width: 36px; height: 36px; border-radius: 50%; background: #ffffff; display: block; }
  .signature .contact { left: 290px; top: 220px; color: var(--crimson); font-size: 21px; font-weight: 500;
    display: flex; align-items: center; gap: 6px; }
</style>
</head>
<body>

  <!-- Letterhead -->
  <section class="piece letterhead" aria-label="Letterhead">
    <div class="brand" style="left:20px; top:26px; gap:12px;">
      <span class="brand-dot" style="width:56px; height:56px;"></span>
      <span class="brand-name" style="font-size:19px;">Nimbara<br>Networks</span>
    </div>
    <div class="abs watermark"></div>
    <div class="abs band"></div>
    <div class="abs band-accent"></div>
  </section>

  <!-- Business card front -->
  <section class="piece card card-front" aria-label="Business card, front">
    <div class="brand" style="left:42px; top:56px; gap:14px;">
      <span class="brand-dot" style="width:76px; height:76px;"></span>
      <span class="brand-name" style="font-size:22px;">Nimbara<br>Networks</span>
    </div>
  </section>

  <!-- Business card back -->
  <section class="piece card card-back" aria-label="Business card, back">
    <div class="brand" style="left:20px; top:10px; gap:6px;">
      <span class="brand-dot" style="width:22px; height:22px;"></span>
      <span class="brand-name" style="font-size:9px;">Nimbara<br>Networks</span>
    </div>
    <div class="abs photo" role="img" aria-label="Portrait photo of the card holder"></div>
    <div class="abs holder">
      <p class="holder-name">Elias Marthen</p>
      <p class="holder-role">Ceo</p>
      <p class="holder-phone">
        <svg width="13" height="13" viewBox="0 0 13 13" aria-hidden="true">
          <circle cx="6.5" cy="6.5" r="6.5" fill="var(--crimson)"/>
          <rect x="4.2" y="2.6" width="4.6" height="7.8" rx="1" fill="none" stroke="#fff" stroke-width="1.1"/>
        </svg>
        555.014.3382
      </p>
    </div>
    <div class="abs band"></div>
  </section>

  <!-- Envelope -->
  <section class="piece envelope" aria-label="Envelope">
    <svg class="abs" style="left:0; top:0;" width="329" height="185" viewBox="0 0 329 185" aria-hidden="true">
      <polyline points="0,0 164,92 329,0" fill="none" stroke="#e1e1e5" stroke-width="1"/>
    </svg>
    <div class="brand" style="left:70px; top:56px; gap:12px;">
      <span class="brand-dot" style="width:70px; height:70px;"></span>
      <span class="brand-name" style="font-size:21px;">Nimbara<br>Networks</span>
    </div>
  </section>

  <!-- Email signature -->
  <section class="piece signature" aria-label="Email signature">
    <div class="abs top"></div>
    <div class="abs photo" role="img" aria-label="Portrait photo of the sender"></div>
    <div class="abs holder">
      <p class="holder-name">Elias Marthen</p>
      <p class="holder-role">Ceo</p>
    </div>
    <div class="abs social" aria-label="Social profile links">
      <span></span><span></span><span></span><span></span>
    </div>
    <p class="abs contact">
      <svg width="26" height="26" viewBox="0 0 26 26" aria-hidden="true">
        <circle cx="13" cy="13" r="13" fill="var(--crimson)"/>
        <rect x="8.5" y="5.5" width="9" height="15" rx="2" fill="none" stroke="#fff" stroke-width="1.8"/>
      </svg>
      555.014.3382
    </p>
    <div class="brand" style="right:36px; top:212px; gap:10px;">
      <span class="brand-dot" style="width:54px; height:54px;"></span>
      <span class="brand-name" style="font-size:17px;">Nimbara<br>Networks</span>
    </div>
  </section>

</body>
</html>
```